web design for specialty coffee shop

We are online shop selling specialty coffeee.
Our brand concept keywords are -
specialty coffee, knowledge, discovery, professional, convenience, collaboration.
there will be five main tabs on the homepage
[home (u icon from logo)]
[coffee]
[equipment]
[gift]
[knowledge]
[about us]
For our site, we will be using the following template.
ONLY DESIGN, NO CODING necessary as our developers will do that.
http://layoutbarn.example/item/velorina-deluxe-adaptive-storefront-theme/full_screen_preview/7351620
Use the template as a base.
You do not have to do exactly the same layout.
Creative Liberty!
For the style and color palette, please look at the attached image.
Our brown logo should match nicely with the style provided in the attachment.
Thank you for taking the time to read this post.
Looking forward to working with artmingle and the amazing designers that are part of this community.
Reason: Dear designers,
I have extended the deadline to give designers who accepted to participate in this contest some more time to submit their designs. Thank you for understanding.

```html
<!DOCTYPE html>
<html lang="en">
<head>
<meta charset="utf-8">
<title>Coffee Shop – Home Sections</title>
<link href="https://fonts.googleapis.com/css2?family=Arimo:ital,wght@0,400;0,700;1,400&family=Ubuntu:wght@400;500;700&display=swap" rel="stylesheet">
<style>
  :root {
    --accent: #f0631f;
    --ink: #222222;
    --body: #5a5a5a;
    --muted: #777777;
    --band: #f4f4f4;
    --rule: #dcdcdc;
    --card-border: #dddddd;
    --btn-top: #82bd3a;
    --btn-bottom: #5f9a1e;
    --btn-edge: #4f8716;
  }
  * { box-sizing: border-box; margin: 0; padding: 0; }
  html, body { width: 958px; height: 1200px; overflow: hidden; background: #fff; }
  body { position: relative; font-family: "Arimo", Arial, sans-serif; color: var(--body); }
  .abs { position: absolute; }
  .accent { color: var(--accent); }

  .section-title { position: absolute; font-size: 18px; color: var(--ink); font-weight: 400; letter-spacing: .2px; }

  /* Beans collection */
  .collection-photo { position: absolute; top: 83px; width: 242px; height: 160px; border: 1px solid #e2e2e2; }
  .collection-caption { position: absolute; top: 252px; width: 242px; text-align: center; }
  .collection-caption h3 { font-size: 14px; font-weight: 400; color: var(--ink); margin-bottom: 2px; }
  .collection-caption p { font-size: 10.5px; line-height: 14.5px; color: var(--muted); text-align: justify; text-align-last: center; word-spacing: 2px; }

  /* Featured band */
  .featured-band { position: absolute; left: 0; top: 364px; width: 958px; height: 377px; background: var(--band); border-top: 1px solid var(--rule); border-bottom: 1px solid var(--rule); }
  .product-card { position: absolute; top: 439px; width: 179px; height: 267px; background: #fff; border: 1px solid var(--card-border); border-radius: 2px; text-align: center; }
  .product-photo { position: absolute; left: 13px; top: 12px; width: 153px; height: 120px; background: radial-gradient(ellipse at 50% 55%, #7a4526 0%, #a86a44 35%, #f4ece6 70%, #ffffff 85%); }
  .product-rule { position: absolute; left: 13px; right: 13px; top: 141px; border-top: 1px solid #cfcfcf; }
  .product-name { position: absolute; left: 0; right: 0; top: 152px; font-family: "Ubuntu", sans-serif; font-weight: 500; font-size: 11.5px; color: var(--accent); }
  .product-desc { position: absolute; left: 10px; right: 10px; top: 171px; font-size: 8.5px; line-height: 11.5px; color: var(--body); }
  .product-price { position: absolute; left: 0; right: 0; top: 199px; font-family: "Ubuntu", sans-serif; font-size: 18px; font-weight: 500; color: #333; }
  .add-to-cart { position: absolute; left: 25px; top: 225px; width: 127px; height: 25px; border: 1px solid var(--btn-edge); border-radius: 2px; background: linear-gradient(var(--btn-top), var(--btn-bottom)); color: #fff; font-family: "Ubuntu", sans-serif; font-weight: 500; font-size: 10px; line-height: 23px; }

  /* Special */
  .special-photo { position: absolute; left: 98px; top: 804px; width: 244px; height: 140px; border: 1px solid #dcdcdc; background: linear-gradient(135deg, #ffffff 0%, #ffffff 40%, #f2ece8 55%, #8a5a3a 80%, #5b3520 100%); }
  .special-text { position: absolute; left: 357px; width: 495px; font-size: 10.5px; line-height: 14.5px; color: var(--body); text-align: justify; word-spacing: 1px; }
  .special-text em { color: var(--accent); }
  .divider { position: absolute; left: 98px; top: 985px; width: 760px; border-top: 1px solid #e4e4e4; }

  /* Testimonials */
  .testimonial-photo { position: absolute; top: 1076px; width: 113px; height: 90px; border: 1px solid #cfcfcf; }
  .testimonial-text { position: absolute; top: 1074px; width: 245px; font-size: 10.5px; line-height: 14.5px; color: var(--body); }
  .testimonial-dash { position: absolute; top: 1143px; font-size: 9px; color: #aaa; }
  .testimonial-name { position: absolute; top: 1155px; font-size: 9px; font-style: italic; color: var(--accent); }
  .slider-arrows { position: absolute; top: 1150px; width: 36px; height: 17px; }
</style>
</head>
<body>

  <!-- Beans collection -->
  <h2 class="section-title" style="left:99px; top:30px;"><span class="accent">Beans</span> Collection</h2>

  <div class="collection-photo" style="left:99px; background:linear-gradient(160deg,#7a2d14,#b0532a 45%,#eae2da 60%,#8e3a18);" role="img" aria-label="White cup filled with coffee beans on a bed of beans"></div>
  <div class="collection-photo" style="left:356px; background:radial-gradient(ellipse at 55% 40%,#c0391e,#9a3418 45%,#e8ddd2 100%);" role="img" aria-label="Ground coffee with whole roasted beans in soft focus"></div>
  <div class="collection-photo" style="left:616px; background:linear-gradient(120deg,#4a2a16,#b08a5a 45%,#e7d9b8 60%,#9b2a20 85%,#5a3018);" role="img" aria-label="Coffee dessert cup beside a scoop of beans and a red napkin"></div>

  <div class="collection-caption" style="left:99px;"><h3>Product Category</h3><p>This is Layoutly's version of Lorem Ipsum. Proin gravida nibh vel velit.</p></div>
  <div class="collection-caption" style="left:356px;"><h3>Product Category</h3><p>This is Layoutly's version of Lorem Ipsum. Proin gravida nibh vel velit.</p></div>
  <div class="collection-caption" style="left:616px;"><h3>Product Category</h3><p>This is Layoutly's version of Lorem Ipsum. Proin gravida nibh vel velit.</p></div>

  <!-- Featured blends -->
  <div class="featured-band"></div>
  <h2 class="section-title" style="left:99px; top:396px;"><span class="accent">Featured</span> Organic Blends</h2>

  <div class="product-card" style="left:98px;">
    <div class="product-photo" role="img" aria-label="Pile of roasted coffee beans"></div>
    <div class="product-rule"></div>
    <div class="product-name">Coffee beans Classica</div>
    <div class="product-desc">This is Layoutly's version of Lorem Ipsum. Proin gravida nibh vel.</div>
    <div class="product-price">$ 500</div>
    <div class="add-to-cart">Add to Cart</div>
  </div>
  <div class="product-card" style="left:292px;">
    <div class="product-photo" role="img" aria-label="Pile of roasted coffee beans"></div>
    <div class="product-rule"></div>
    <div class="product-name">Coffee beans Classica</div>
    <div class="product-desc">This is Layoutly's version of Lorem Ipsum. Proin gravida nibh vel.</div>
    <div class="product-price">$ 500</div>
    <div class="add-to-cart">Add to Cart</div>
  </div>
  <div class="product-card" style="left:485px;">
    <div class="product-photo" role="img" aria-label="Pile of roasted coffee beans"></div>
    <div class="product-rule"></div>
    <div class="product-name">Coffee beans Classica</div>
    <div class="product-desc">This is Layoutly's version of Lorem Ipsum. Proin gravida nibh vel.</div>
    <div class="product-price">$ 500</div>
    <div class="add-to-cart">Add to Cart</div>
  </div>
  <div class="product-card" style="left:678px;">
    <div class="product-photo" role="img" aria-label="Pile of roasted coffee beans"></div>
    <div class="product-rule"></div>
    <div class="product-name">Coffee beans Classica</div>
    <div class="product-desc">This is Layoutly's version of Lorem Ipsum. Proin gravida nibh vel.</div>
    <div class="product-price">$ 500</div>
    <div class="add-to-cart">Add to Cart</div>
  </div>

  <!-- What makes us special -->
  <div class="special-photo" role="img" aria-label="Tipped white cup and saucer spilling coffee beans"></div>
  <h2 class="section-title" style="left:357px; top:803px;"><span class="accent">What makes us</span> special</h2>
  <p class="special-text" style="top:836px;">This is Layoutly's version of <em>Lorem Ipsum.</em> Proin gravida nibh vel velit auctor aliquet. Aenean sollicitudin, lorem quis bibendum auctor, nisi elit consequat ipsum, nec sagittis sem nibh id elit. Duis sed odio sit amet nibh vulputate cursus a sit amet mauris. Morbi accumsan ipsum velit. Nam nec tellus a odio tincidunt auctor a ornare odio.</p>
  <p class="special-text" style="top:898px;">Sed non mauris <em>vitae erat consequat</em> auctor eu in elit. Class aptent taciti sociosqu ad <em>litora torquent</em> per conubia nostra, per inceptos himenaeos.</p>

  <div class="divider"></div>

  <!-- Testimonials -->
  <h2 class="section-title" style="left:0; width:958px; text-align:center; top:1027px;">What <span class="accent">Customers</span> are saying</h2>

  <div class="testimonial-photo" style="left:99px; background:linear-gradient(135deg,#c9c08a,#e3c6a4 50%,#8f9a52);" role="img" aria-label="Portrait of a smiling customer"></div>
  <p class="testimonial-text" style="left:220px;">This is Layoutly's version of Lorem Ipsum. Proin gravida nibh vel velit auctor aliquet. Aenean sollicitudin, lorem quis bibendum auctor, nisi elit consequat ipsum, nec sagittis sem nibh id elit.</p>
  <div class="testimonial-dash" style="left:220px;">--</div>
  <div class="testimonial-name" style="left:220px;">Mira Dolven</div>
  <svg class="slider-arrows" style="left:434px;" viewBox="0 0 36 17" aria-hidden="true">
    <rect x="0.5" y="0.5" width="35" height="16" rx="2" fill="#f2f2f2" stroke="#aaa"/>
    <line x1="18" y1="1" x2="18" y2="16" stroke="#aaa"/>
    <path d="M10.5 5.5 L7 8.5 L10.5 11.5Z" fill="#555"/>
    <path d="M25.5 5.5 L29 8.5 L25.5 11.5Z" fill="#555"/>
  </svg>

  <div class="testimonial-photo" style="left:485px; background:linear-gradient(135deg,#f2f2f2,#d8c2b0 50%,#6a7a90);" role="img" aria-label="Portrait of a grey-haired customer"></div>
  <p class="testimonial-text" style="left:606px;">This is Layoutly's version of Lorem Ipsum. Proin gravida nibh vel velit auctor aliquet. Aenean sollicitudin, lorem quis bibendum auctor, nisi elit consequat ipsum, nec sagittis sem nibh id elit.</p>
  <div class="testimonial-dash" style="left:606px;">--</div>
  <div class="testimonial-name" style="left:606px;">Mira Dolven</div>
  <svg class="slider-arrows" style="left:820px;" viewBox="0 0 36 17" aria-hidden="true">
    <rect x="0.5" y="0.5" width="35" height="16" rx="2" fill="#f2f2f2" stroke="#aaa"/>
    <line x1="18" y1="1" x2="18" y2="16" stroke="#aaa"/>
    <path d="M10.5 5.5 L7 8.5 L10.5 11.5Z" fill="#555"/>
    <path d="M25.5 5.5 L29 8.5 L25.5 11.5Z" fill="#555"/>
  </svg>

</body>
</html>
```